Corporate Business Card

Very professional, Modern, Not to busy, include phone address email, website
(253) 555-0174, 61807 19th Street N, Kent, WA 98517, marcus@kestrelbayholding.com, brelvanindustries.com

Target Market(s)

Manufacturing

Industry/Entity Type

Aero, machining, manufacturing, Off road racing

Contact Information for Business Card

Phone, address email, website

```html
<!DOCTYPE html>
<html lang="en">
<head>
<meta charset="utf-8">
<title>Brelvan Industries – Business Card</title>
<link rel="stylesheet" href="https://fonts.googleapis.com/css2?family=Montserrat:ital,wght@0,500;0,700;0,800;1,800&display=swap">
<style>
  :root {
    --navy: #273c73;
    --red: #d4282f;
    --white: #ffffff;
    --ink: #1b1b1b;
    --backdrop: #f5f5f5;
  }
  * { box-sizing: border-box; margin: 0; padding: 0; }
  html, body { width: 1200px; height: 1057px; overflow: hidden; }
  body {
    background: var(--backdrop);
    font-family: "Montserrat", Arial, sans-serif;
    position: relative;
  }
  .card {
    position: absolute;
    left: 333px;
    width: 533px;
    height: 304px;
    overflow: hidden;
  }
  .card-front { top: 194px; background: var(--navy); }
  .card-back { top: 559px; background: var(--white); }

  .edge-band {
    position: absolute;
    left: 0; bottom: 0;
    width: 100%;
    height: 15px;
    display: flex;
  }
  .edge-band .accent { width: 59px; background: var(--red); }
  .edge-band .rest { flex: 1; }
  .card-front .edge-band .rest { background: var(--white); }
  .card-back .edge-band .rest { background: var(--navy); }

  .wordmark {
    position: absolute;
    display: flex;
    align-items: center;
    gap: 10px;
    font-weight: 800;
    white-space: nowrap;
  }
  .wordmark .mark-square { background: var(--red); flex: none; }
  .card-front .wordmark {
    left: 0; right: 0; top: 135px;
    justify-content: center;
    color: var(--white);
    font-size: 30px;
    letter-spacing: 0.5px;
  }
  .card-front .mark-square { width: 22px; height: 22px; }
  .card-back .wordmark {
    right: 34px; top: 44px;
    color: var(--navy);
    font-size: 15px;
    gap: 7px;
  }
  .card-back .mark-square { width: 12px; height: 12px; }

  .holder { position: absolute; left: 50px; top: 121px; }
  .holder-name {
    color: var(--navy);
    font-weight: 700;
    font-size: 27px;
    letter-spacing: -0.5px;
    line-height: 1.1;
  }
  .holder-role {
    color: var(--red);
    font-weight: 800;
    font-style: italic;
    font-size: 11px;
    letter-spacing: 2.6px;
    line-height: 1.2;
  }

  .contact-list { position: absolute; left: 50px; top: 180px; list-style: none; }
  .contact-list li {
    display: flex;
    align-items: center;
    gap: 7px;
    height: 20.5px;
    font-size: 10px;
    font-weight: 500;
    color: var(--ink);
  }
  .contact-list svg { width: 10px; height: 10px; flex: none; fill: var(--ink); }
</style>
</head>
<body>

<section class="card card-front" aria-label="Card front">
  <div class="wordmark"><span class="mark-square"></span>Brelvan Industries</div>
  <div class="edge-band"><span class="accent"></span><span class="rest"></span></div>
</section>

<section class="card card-back" aria-label="Card back">
  <div class="wordmark"><span class="mark-square"></span>Brelvan Industries</div>

  <div class="holder">
    <p class="holder-name">Your Name</p>
    <p class="holder-role">POSITION</p>
  </div>

  <ul class="contact-list">
    <li>
      <svg viewBox="0 0 24 24" aria-hidden="true"><path d="M6.6 10.8a15.1 15.1 0 0 0 6.6 6.6l2.2-2.2a1 1 0 0 1 1-.25 11.4 11.4 0 0 0 3.6.57 1 1 0 0 1 1 1V20a1 1 0 0 1-1 1A17 17 0 0 1 3 4a1 1 0 0 1 1-1h3.5a1 1 0 0 1 1 1c0 1.25.2 2.45.57 3.57a1 1 0 0 1-.25 1z"/></svg>
      (253) 555-0174, 61807
    </li>
    <li>
      <svg viewBox="0 0 24 24" aria-hidden="true"><path d="M12 2a7 7 0 0 0-7 7c0 5.2 7 13 7 13s7-7.8 7-13a7 7 0 0 0-7-7zm0 9.5A2.5 2.5 0 1 1 12 6.5a2.5 2.5 0 0 1 0 5z"/></svg>
      61807 19th Street N, Kent, WA 98517
    </li>
    <li>
      <svg viewBox="0 0 24 24" aria-hidden="true"><path d="M12 2a10 10 0 1 0 0 20 10 10 0 0 0 0-20zm6.9 6h-2.9a15.6 15.6 0 0 0-1.4-3.6A8 8 0 0 1 18.9 8zM12 4c.8 1.2 1.5 2.5 1.9 4h-3.8c.4-1.5 1.1-2.8 1.9-4zM4.3 14a8.2 8.2 0 0 1 0-4h3.4a16.5 16.5 0 0 0 0 4zm.8 2h2.9c.3 1.3.8 2.5 1.4 3.6A8 8 0 0 1 5.1 16zM8 8H5.1a8 8 0 0 1 4.3-3.6C8.8 5.5 8.3 6.7 8 8zm4 12c-.8-1.2-1.5-2.5-1.9-4h3.8c-.4 1.5-1.1 2.8-1.9 4zm2.3-6H9.7a14.7 14.7 0 0 1 0-4h4.6a14.7 14.7 0 0 1 0 4zm.3 5.6c.6-1.1 1.1-2.3 1.4-3.6h2.9a8 8 0 0 1-4.3 3.6zm1.7-5.6a16.5 16.5 0 0 0 0-4h3.4a8.2 8.2 0 0 1 0 4z"/></svg>
      brelvanindustries.com
    </li>
    <li>
      <svg viewBox="0 0 24 24" aria-hidden="true"><path d="M2 5h20v14H2zm2 2v.5l8 5 8-5V7l-8 5z"/></svg>
      marcus@kestrelbayholding.com
    </li>
  </ul>

  <div class="edge-band"><span class="accent"></span><span class="rest"></span></div>
</section>

</body>
</html>
```